FotoVELTA buisnesscard

Hey :) I need a modern buisnesscard for my company FotoVELTA
It most have:
Dagligleder og Fotograf: Henrik Torvald Bjelland

Mob: +4791642058
Epost: post@fotovelta.no
Adresse: Bakkestien22, 6291 Havnøy

Facbook and instagram logo with text FotoVELTA

FotoVELTA logo

It Company

```html
<!DOCTYPE html>
<html lang="no">
<head>
<meta charset="utf-8">
<title>FotoVELTA – visittkort</title>
<link href="https://fonts.googleapis.com/css2?family=Poppins:wght@300;500;600&display=swap" rel="stylesheet">
<style>
  :root {
    --backdrop: #d8d3cb;
    --card-dark: #1b1d1e;
    --card-mid: #34383a;
    --ink-light: #ececec;
    --ink-soft: #c9cbcc;
    --icon-bg: #e4e4e4;
    --icon-ink: #2a2c2d;
  }
  * { margin: 0; padding: 0; box-sizing: border-box; }
  html, body { width: 1200px; height: 858px; overflow: hidden; }
  body {
    background: var(--backdrop);
    font-family: "Poppins", sans-serif;
    display: flex;
    align-items: center;
    justify-content: center;
    gap: 40px;
  }
  .card {
    position: relative;
    width: 540px;
    height: 309px;
    border-radius: 4px;
    background: linear-gradient(135deg, var(--card-mid) 0%, var(--card-dark) 70%);
    box-shadow: 0 14px 30px rgba(0,0,0,0.28);
    color: var(--ink-light);
    overflow: hidden;
  }
  .brand { display: flex; align-items: center; gap: 14px; }
  .brand-square { width: 40px; height: 40px; background: var(--ink-light); }
  .brand-name { font-weight: 600; font-size: 46px; letter-spacing: 0.5px; line-height: 1; }

  .card-front .brand { position: absolute; left: 44px; top: 54px; }
  .details {
    position: absolute;
    left: 44px; right: 30px; bottom: 56px;
    display: flex;
    align-items: center;
  }
  .person { width: 226px; }
  .person-name { font-weight: 600; font-size: 16px; color: var(--ink-soft); }
  .person-role { font-weight: 300; font-size: 13px; color: var(--ink-soft); margin-top: 2px; }
  .divider { width: 1px; height: 58px; background: var(--ink-soft); margin: 0 16px 0 4px; }
  .contacts { list-style: none; }
  .contacts li {
    display: flex; align-items: center; gap: 8px;
    font-weight: 300; font-size: 12px; color: var(--ink-soft);
    line-height: 20px;
  }
  .contacts svg { width: 13px; height: 13px; flex: none; }

  .card-back .brand {
    position: absolute; left: 50%; top: 50%;
    transform: translate(-50%, -50%);
  }
  .card-back .brand-square { width: 50px; height: 50px; }
  .card-back .brand-name { font-size: 58px; }
</style>
</head>
<body>

<section class="card card-front" aria-label="Visittkort forside">
  <div class="brand">
    <span class="brand-square"></span>
    <span class="brand-name">FotoVELTA</span>
  </div>
  <div class="details">
    <div class="person">
      <p class="person-name">Henrik Torvald Bjelland</p>
      <p class="person-role">Dagligleder og Fotograf</p>
    </div>
    <span class="divider"></span>
    <ul class="contacts">
      <li>
        <svg viewBox="0 0 13 13" aria-hidden="true"><rect width="13" height="13" rx="2" fill="var(--icon-bg)"/><rect x="4" y="2" width="5" height="9" rx="1" fill="none" stroke="var(--icon-ink)" stroke-width="1.2"/></svg>
        +4791642058
      </li>
      <li>
        <svg viewBox="0 0 13 13" aria-hidden="true"><rect width="13" height="13" rx="2" fill="var(--icon-bg)"/><rect x="2.5" y="4" width="8" height="5.5" fill="none" stroke="var(--icon-ink)" stroke-width="1.1"/><path d="M2.5 4 L6.5 7 L10.5 4" fill="none" stroke="var(--icon-ink)" stroke-width="1.1"/></svg>
        post@fotovelta.no
      </li>
      <li>
        <svg viewBox="0 0 13 13" aria-hidden="true"><rect width="13" height="13" rx="2" fill="var(--icon-bg)"/><path d="M6.5 11 C4 8 3.5 6.8 3.5 5.5 A3 3 0 0 1 9.5 5.5 C9.5 6.8 9 8 6.5 11 Z" fill="var(--icon-ink)"/><circle cx="6.5" cy="5.5" r="1.1" fill="var(--icon-bg)"/></svg>
        Bakkestien22, 6291 Havnøy
      </li>
    </ul>
  </div>
</section>

<section class="card card-back" aria-label="Visittkort bakside">
  <div class="brand">
    <span class="brand-square"></span>
    <span class="brand-name">FotoVELTA</span>
  </div>
</section>

</body>
</html>
```